Home page improvements

We're looking for a designer to make changes to the home page of our site www.mendlark.com to:
a) include space for a featured article or blog
b) reduce the size of the ad and to create more ads for rotation
c) include space for special offers (2-3 featured repairs) - these can be links to the detailed repair page.
We're not looking for substantial redesign. We will have other design tasks on an ongoing basis for the winning designer, so an indication of hourly charge-out rate would be appreciated.
You're welcome to submit other changes you feel would benefit the site also.
Look and feel
Each slider illustrates characteristics of the customer's brand and the style your logo design should communicate.

```html
<!DOCTYPE html>
<html lang="en">
<head>
<meta charset="utf-8">
<title>Mendlark — Fixed. Guaranteed.</title>
<link href="https://fonts.googleapis.com/css2?family=Arimo:wght@400;700&family=Open+Sans:wght@400;700&display=swap" rel="stylesheet">
<style>
:root{
  --sky:#4fb3e8;
  --brand:#3fa9e6;
  --ink:#2b2b2b;
  --text:#333;
  --muted:#888;
  --page:#fff;
  --ground:#ededed;
  --panel:#eeeeee;
  --bar:#2a2a2a;
  --navy:#1c3550;
}
*{box-sizing:border-box;margin:0;padding:0}
html,body{width:876px;height:1200px;overflow:hidden}
body{position:relative;font-family:"Arimo",Arial,sans-serif;color:var(--text);
  background:linear-gradient(var(--sky) 0 422px,var(--ground) 422px)}
.abs{position:absolute}
.page{left:25px;top:30px;width:823px;height:1080px;background:var(--page)}
.logo{left:62px;top:50px;display:flex;align-items:center;gap:14px}
.logo-name{font-size:46px;font-weight:700;color:#444;letter-spacing:-1px;line-height:1}
.logo-mark{width:44px;height:74px;background:var(--brand);border-radius:6px}
.tagline{left:54px;top:110px;font-size:19px;color:var(--brand)}
.utility{left:489px;top:44px;font-size:12px;color:#111;display:flex;gap:7px;align-items:center;white-space:nowrap}
.utility .country{background:#e6e6e6;font-weight:700;padding:1px 26px 1px 10px;margin-right:20px}
.nav{left:38px;top:155px;width:798px;height:42px;display:flex;gap:2px}
.nav a{flex:1;background:var(--ink);color:#fff;text-decoration:none;display:flex;align-items:center;justify-content:center;font-size:16px;white-space:nowrap}
.nav a.current{background:var(--brand)}
.nav a.small{font-size:13px}
.hero{left:37px;top:204px;width:801px;height:283px;background:linear-gradient(90deg,#2e8fd0,#5bb8ee 50%,#2e8fd0);overflow:hidden;font-family:"Open Sans",sans-serif;color:#fff}
.hero-title{left:93px;top:98px;font-size:46px;font-weight:700;line-height:1;white-space:nowrap}
.hero-sub{left:188px;top:146px;font-size:36px;line-height:1;white-space:nowrap}
.hero-line{left:56px;top:186px;font-size:14px;white-space:nowrap}
.hero-device{left:417px;top:10px;width:112px;height:226px;border-radius:16px;background:linear-gradient(#333,#111)}
.hero-arrow{top:110px}
.cta{left:555px;top:168px;width:228px;height:56px;border:2px solid #1d5f99;border-radius:5px;background:linear-gradient(#4a90cf,#1f5f9c);text-align:center}
.cta b{display:block;font-family:"Arimo",sans-serif;font-size:30px;line-height:34px;margin-top:2px}
.cta small{display:block;font-size:9px}
.learn{left:537px;top:230px;height:28px;font-family:"Arimo",sans-serif;font-size:21px;line-height:28px;display:flex;align-items:center;gap:6px;white-space:nowrap}
.learn em{font-style:normal;color:var(--navy)}
.tour-tag{margin-left:0;height:18px;line-height:18px;background:#8ec9ef;color:var(--navy);font-size:9px;padding:0 22px 0 6px;white-space:nowrap;clip-path:polygon(0 0,86% 0,100% 50%,86% 100%,0 100%)}
.dots{left:23px;top:244px;display:flex;gap:7px}
.dots span{width:30px;height:30px;border-radius:50%;background:var(--ink);color:#fff;font-size:16px;display:flex;align-items:center;justify-content:center;font-family:"Arimo",sans-serif}
.dots span.on{background:#fff;color:#222}
.feature{left:38px;width:188px}
.feature h3{height:52px;background:var(--brand);color:#fff;font-weight:400;font-size:15px;display:flex;align-items:center;padding-left:18px;gap:12px}
.feature h3::before{content:"";width:13px;height:13px;border-radius:50%;background:#fff}
.feature p{background:var(--panel);color:var(--muted);font-size:10.5px;line-height:13px;padding:6px 10px 10px}
.divider{left:238px;top:498px;width:1px;height:240px;background:#ccc}
.blog{left:246px;top:498px;width:590px}
.blog h2{font-weight:400;font-size:30px;color:#222;margin-bottom:4px}
.blog p{font-size:12.4px;line-height:15.6px;color:#333;padding-left:4px;margin-bottom:15px}
.offer{top:769px;width:196px}
.offer .visual{height:145px;border:3px solid #ddd}
.offer h4{font-size:15.5px;margin:16px 0 0 12px;color:#111;white-space:nowrap}
.offer .lede{font-size:10px;text-align:center;color:#111;white-space:nowrap}
.offer .body{font-size:9.6px;line-height:12px;color:var(--muted);margin:12px 10px 0 6px;height:50px}
.offer .more{display:inline-block;margin-top:10px;background:var(--ink);color:#fff;font-size:18px;padding:3px 15px;text-decoration:none}
.offer-rule{top:937px;width:1px;height:80px;background:#ccc}
.foot-col{top:1114px;font-size:11.5px;white-space:nowrap}
.foot-col h5{font-weight:400;color:var(--brand);font-size:14px}
.foot-col nav{color:#111;margin-top:3px}
.foot-col nav span+span{border-left:1px solid #111;padding-left:4px;margin-left:3px}
.bottom{left:25px;top:1160px;width:823px;height:40px;background:var(--bar);color:#fff;font-size:13px}
.cards{left:14px;top:9px;display:flex;gap:5px}
.cards span{width:34px;height:21px;background:#f2f2f2;border-radius:2px}
.copy{right:18px;top:13px}
</style>
</head>
<body>
<div class="abs page"></div>

<header>
  <div class="abs logo"><span class="logo-name">mendlark</span><span class="logo-mark"></span></div>
  <div class="abs tagline">Fixed.Guaranteed.</div>
  <div class="abs utility"><span>Location</span><span class="country">United States</span><span>Find Us</span><span>Contact Us</span><span>Log in</span></div>
  <nav class="abs nav">
    <a class="current" href="#">Home</a><a href="#">Aobut Us</a><a class="small" href="#">Repairs &amp; pricing</a><a href="#">Tour</a><a href="#">Why choose us</a><a href="#">FAQ's</a><a href="#">Blog</a>
  </nav>
</header>

<section class="abs hero">
  <svg class="abs hero-arrow" style="left:10px" width="24" height="40" viewBox="0 0 24 40"><path d="M20 4 6 20l14 16" fill="none" stroke="#fff" stroke-width="6"/></svg>
  <svg class="abs hero-arrow" style="right:10px" width="24" height="40" viewBox="0 0 24 40"><path d="M4 4l14 16L4 36" fill="none" stroke="#fff" stroke-width="6"/></svg>
  <div class="abs hero-title">10,000 repairs</div>
  <div class="abs hero-sub">and counting.</div>
  <div class="abs hero-line">When it comes to experience, no one else comes close.</div>
  <div class="abs hero-device" role="img" aria-label="Smartphone product photo"></div>
  <div class="abs cta"><b>REPAIRS</b><small>NO PAYMENT UNTIL IT IS FIXED</small></div>
  <div class="abs learn">or <em>LEARN MORE</em><span class="tour-tag">TAKE THE TOUR</span></div>
  <div class="abs dots"><span>1</span><span class="on">2</span><span>3</span><span>4</span></div>
</section>

<aside>
  <div class="abs feature" style="top:494px"><h3>What do we fix?</h3><p>Smartphones and players, from broken screens to headphone jacks to home keysand everything else in between.</p></div>
  <div class="abs feature" style="top:625px"><h3>What do we fix?</h3><p>Smartphones and players, from broken screens to headphone jacks to home keysand everything else in between.</p></div>
  <div class="abs feature" style="top:761px"><h3>What do we fix?</h3><p>Smartphones and players, from broken screens to headphone jacks to home keysand everything else in between.</p></div>
  <div class="abs feature" style="top:892px"><h3>What do we fix?</h3><p>Smartphones and players, from broken screens to headphone jacks to home keysand everything else in between.</p></div>
</aside>

<div class="abs divider"></div>
<article class="abs blog">
  <h2>Blog</h2>
  <p>Lorem ipsum dolor sit amet, consectetur adipisicing elit,sed do eiusmod tempor incididunt ut labore et dolore magna.Lorem ipsum dolor sit amet, consectetur adipisicing elit,sed do eiusmod tempor incididu nt ut labore et dolore magna.Lorem ipsum dolor sit amet, consectetur adipisicing elit,sed do eiusmod tempor incididunt ut labore et dolore magna.Lorem ipsum dolor sit amet, consectetur adipisicing elit,sed do eiusmod tempor incididu nt ut labore et dolore magna.Lorem ipsum dolor sit amet, consectetur adipisicing elit,sed do eiusmod tempor incididunt ut labore et dolore magna.Lorem ipsum dolor sit amet, consectetur adipisicing elit,sed do eiusmod tempor incididunt ut labore et dolore magna.</p>
  <p>Lorem ipsum dolor sit amet, consectetur adipisicing elit,sed do eiusmod tempor incididunt ut labore et dolore magna.Lorem ipsum dolor sit amet, consectetur adipisicing elit,sed do eiusmod tempor incididu nt ut labore et dolore magna.Lorem ipsum dolor sit amet, consectetur adipisicing elit,sed do eiusmod tempor incididunt ut labore et dolore magna.Lorem ipsum dolor sit amet, consectetur adipisicing elit,sed do eiusmod tempor incididu nt ut labore et dolore magna.</p>
</article>

<section>
  <div class="abs offer" style="left:236px">
    <div class="visual" role="img" aria-label="City street map with a red 'fixed in 30 minutes' badge" style="background:linear-gradient(135deg,#e9e4d6,#d8d3c2)"></div>
    <h4>In New York City?</h4><div class="lede">Visit our workshop SoHo.</div>
    <p class="body">Praesent tibulum molestie lacueno mera yhe ndrerit mauris ketyade. Phasellus porta. Fusce suscipit vari uslasera. Cum soci iseras natoque nertyades.........</p>
    <a class="more" href="#">More</a>
  </div>
  <div class="abs offer-rule" style="left:436px"></div>
  <div class="abs offer" style="left:439px">
    <div class="visual" role="img" aria-label="Cargo jet flying in a blue sky" style="background:linear-gradient(#2f6fc4,#8db8e6)"></div>
    <h4>Premium mail-in service.</h4><div class="lede">Back in a flash - 24 hour turnaround.</div>
    <p class="body">Praesent tibulum molestie lacueno mera yhe ndrerit mauris ketyade. Phasellus porta. Fusce suscipit vari uslasera. Cum soci iseras natoque nertyades.........</p>
    <a class="more" href="#">More</a>
  </div>
  <div class="abs offer-rule" style="left:639px"></div>
  <div class="abs offer" style="left:642px">
    <div class="visual" role="img" aria-label="Comparison table of repair services" style="background:linear-gradient(#f7f7f7,#e4e4e4)"></div>
    <h4>Better in every way</h4><div class="lede">There's no comparison.</div>
    <p class="body">Praesent tibulum molestie lacueno mera yhe ndrerit mauris ketyade. Phasellus porta. Fusce suscipit vari uslasera. Cum soci iseras natoque nertyades.........</p>
    <a class="more" href="#">More</a>
  </div>
</section>

<footer>
  <div class="abs foot-col" style="left:38px"><h5>More info</h5><nav><span>Shipping policy</span><span>Warranty policy</span><span>Terms &amp; conditions</span></nav></div>
  <div class="abs foot-col" style="left:354px"><h5>About us</h5><nav><span>Our story</span><span>Guarantee</span><span>Careers</span></nav></div>
  <div class="abs foot-col" style="left:540px"><h5>Questions?</h5><nav><span>FAQ</span><span>Contact us</span><span>Take the tour</span></nav></div>
  <div class="abs bottom">
    <div class="abs cards"><span></span><span></span><span></span><span></span></div>
    <div class="abs copy">Copyright@2012 Mendlark LLC</div>
  </div>
</footer>
</body>
</html>
```